Varga Lillas Physiotherapy Business Card Vienna

We need a business card design for a newly created Physiotherapy company based in Vienna Austria.
We seek a simple, modern, minimalist design without too much color variation. The font should look young/fresh, but definitely not childish or so. Since we are a starting Business, we currently haven't got a logo, if you feel like a logo would fit your design, feel free to use one, but it's not necessary.
Target Market(s)
Healthcare, young and elderly people with mobility issues
Industry/Entity Type
Health And Wellness
Contact Information for Business Card
Name: Lilla Varga
Title description: Physiotherapist
Phone num: +43 664 5290 4816
e-mail: lilla.praxis@brelomail.com
Colors
Designer to choose colors to be used in the design.
Requirements
Must have
- Final design language must be in German, basically, the Title Description needs to be "Physiotherapeutin" the other details remain as in the English Language.
Nice to have
- Simple, modern, minimalist design
Should not have
- too many colors, Obvious use of a skeleton, skull, spline

```html
<!DOCTYPE html>
<html lang="de">
<head>
<meta charset="utf-8">
<title>Varga Lillas Physiotherapy – Visitenkarte</title>
<link rel="stylesheet" href="https://fonts.googleapis.com/css2?family=Open+Sans:ital,wght@0,400;1,400&display=swap">
<style>
  :root {
    --page-bg: #eeeeec;
    --card-black: #1b1b1b;
    --card-white: #fbfbfa;
    --foil-silver: #c9c9c9;
    --ink: #1e1e1e;
    --ink-soft: #3a3a3a;
    --edge: #d8d8d6;
  }
  * { margin: 0; padding: 0; box-sizing: border-box; }
  html, body {
    width: 1200px;
    height: 775px;
    overflow: hidden;
    background: var(--page-bg);
  }
  .canvas {
    position: relative;
    width: 1200px;
    height: 775px;
  }
  .card {
    position: absolute;
    top: 150px;
    width: 520px;
    height: 300px;
    border-radius: 3px;
    box-shadow: 0 6px 18px rgba(0,0,0,0.12);
  }
  .card--front {
    left: 60px;
    background: var(--card-black);
    display: flex;
    align-items: center;
    justify-content: center;
  }
  .card--back {
    left: 620px;
    background: var(--card-white);
    border: 1px solid var(--edge);
  }
  .brand-name {
    font-family: "Open Sans", sans-serif;
    font-weight: 400;
    text-align: center;
    white-space: nowrap;
  }
  .brand-name__line {
    display: block;
    font-size: 40px;
    letter-spacing: 1px;
    line-height: 1.1;
  }
  .brand-name__field {
    display: block;
    font-size: 16px;
    letter-spacing: 10px;
    margin-top: 8px;
    padding-left: 10px;
  }
  .card--front .brand-name { color: var(--foil-silver); }
  .holder {
    position: absolute;
    left: 50px;
    top: 48px;
    font-family: "Open Sans", sans-serif;
    color: var(--ink);
  }
  .holder__name {
    font-size: 19px;
    letter-spacing: 0.5px;
  }
  .holder__title {
    font-size: 12px;
    font-style: italic;
    color: var(--ink-soft);
    margin-top: 2px;
  }
  .contact {
    position: absolute;
    left: 190px;
    top: 170px;
    list-style: none;
    font-family: "Open Sans", sans-serif;
    font-size: 13px;
    color: var(--ink);
  }
  .contact__item {
    display: flex;
    align-items: center;
    gap: 10px;
    margin-bottom: 8px;
  }
  .contact__icon { width: 12px; height: 12px; flex: none; }
  .lockup {
    position: absolute;
    left: 752px;
    top: 640px;
    color: var(--ink);
  }
  .lockup .brand-name__line { font-size: 40px; }
  .lockup .brand-name__field { letter-spacing: 9px; padding-left: 9px; }
</style>
</head>
<body>
<main class="canvas">
  <section class="card card--front" aria-label="Vorderseite">
    <div class="brand-name">
      <span class="brand-name__line">VARGA LILLAS</span>
      <span class="brand-name__field">PHYSIOTHERAPY</span>
    </div>
  </section>

  <section class="card card--back" aria-label="Rückseite">
    <div class="holder">
      <p class="holder__name">LILLA VARGA</p>
      <p class="holder__title">Physiotherapeutin</p>
    </div>
    <ul class="contact">
      <li class="contact__item">
        <svg class="contact__icon" viewBox="0 0 12 12" aria-hidden="true">
          <rect width="12" height="12" rx="2" fill="#1e1e1e"/>
          <path d="M3.6 2.8l1.2 1.6-.7.8c.4.9 1 1.5 1.9 1.9l.8-.7 1.6 1.2-.6 1.2C5.6 8.6 3.4 6.4 3.2 3.4z" fill="#fff"/>
        </svg>
        <span>+43 664 5290 4816</span>
      </li>
      <li class="contact__item">
        <svg class="contact__icon" viewBox="0 0 12 12" aria-hidden="true">
          <rect width="12" height="12" rx="2" fill="#1e1e1e"/>
          <rect x="2.5" y="3.5" width="7" height="5" fill="none" stroke="#fff" stroke-width="0.9"/>
          <path d="M2.5 3.5L6 6.3 9.5 3.5" fill="none" stroke="#fff" stroke-width="0.9"/>
        </svg>
        <span>lilla.praxis@brelomail.com</span>
      </li>
    </ul>
  </section>

  <div class="lockup brand-name">
    <span class="brand-name__line">VARGA LILLAS</span>
    <span class="brand-name__field">PHYSIOTHERAPY</span>
  </div>
</main>
</body>
</html>
```